We are looking to improve our packaging, because we are wanting to secure our products into five star hotels, spa and wellness centres and maybe even high end retail department stores. That is why it is important it must look the part. We are even prepared to change our current packaging (White stand up pouches) for something different e.g box etc...

Please keep in mind when designing our new Serenova packaging that our product range will extend to Room Sprays, Candles, Diffuser, Essential Oils, Soaps, Body Scrubs, Milk Baths, Body Lotions, Face Products. So the design will need to compliment and we must be able to adjust the artwork with ease to fit bottles big and small, tubes, boxes glass jars etc... at later stage.

Please see inspiration images of packaging I like. But please do not copy them. We would like something that is unique to our brand that will last for 2-4 years before we have to change the packaging again.

Our current packaging is in a white stand up pouches.
Updates

Project Deadline Extended Reason: Hi All,I have decided to extend the Serenova Calm Infusion Packaging project as the designs I have received are not what I am looking for and are not polished enough for the retail health and spa market. Some of the ideas I received are on the right track, but they need to be reworked a bit more to give our packaging a premium high end looking product. I am trying to get our products into large retail outlets department stores, Chemists, Health and natural product stores, 5 star spa resorts and hotels and eventually export it globally and with so many similar products available for sale our products needs to stand out from the rest of the competition. We use premium grade salts with natural and organic ingredients in our products when we make them. They do not have any harsh chemicals in them. At the moment I am keeping to the stand up white pouches for now, but this will change later this year to a box. We have a good product that sells well, but our current look and feel of our packaging is letting us down and making it difficult to market into the bigger retail stores. I have attached a few sample ideas of what we like, but with our own unique mark to it. We would like something that is unique to us to give our Serenova brand its own identity. I will leave this up to your creative skills.Our Serenova product range will branch out to the following in a couple of months. Body Scrubs, Liquid Soaps, Soaps, Body and Face Lotions, Milk baths, Bath and Spa Tea Bags, Bubble Paths, Herbal and Fragranced Bath & Spa products, Steam Therapy, Massage and Bath Oils, Room Sprays, Home Fragrances and Essential oils. So please keep this mind when designing a label that it must be easily adapted to different shapes and size products. e.g. boxes, jars, tubes and bottles.If you have any question before you start, please send me a message.Thank you for taking the time to read our extended brief and very excited to see your designs. Kind Regards, Added Saturday, January 9, 2016

Target Market(s)

Male and female, natural products, well-being, holistic, wellness centres, spa resorts, 5 stars hotels and upmarket.

Industry/Entity Type

Health And Wellness

Font styles to use
Serif
Sans Serif
Other font styles liked:
• Open Sans

Requirements
Must have
• Front: Company Name: Brand name Serenova Calm Infusion (See logo attached or feel fry to add your design flair to this). Please insert Front Packaging copy, 100% pure & natural logo, weight of item 1kg
• Back: Valtek logo (attached), Australian Packed & Owned logo (attached or you can just use type), Please use Back Packaging copy attached. Please allow space for barcode, Batch number and expiry date.
Nice to have
• Vector background, natural earthy feel, natural or organic textures
• but we are open to any suggestions you might have.

```html
<!DOCTYPE html>
<html lang="en">
<head>
<meta charset="UTF-8">
<title>Serenova Calm Infusion – Pouch Front</title>
<link rel="stylesheet" href="https://fonts.googleapis.com/css2?family=Open+Sans:wght@400;600;700&family=Marcellus&family=Cormorant+Garamond:wght@500&display=swap">
<style>
  :root {
    --paper: #ffffff;
    --ink: #111111;
    --ink-soft: #2a2a2a;
    --wash-pink: #f2a6dc;
    --wash-blue: #a9d8f0;
    --wash-green: #bfe6b0;
    --wash-yellow: #f6e79a;
  }
  * { margin: 0; padding: 0; box-sizing: border-box; }
  html, body { width: 1200px; height: 1200px; overflow: hidden; background: var(--paper); }
  .pouch-front {
    position: relative;
    width: 1200px;
    height: 1200px;
    background: var(--paper);
    color: var(--ink);
  }
  .artwork-wash {
    position: absolute;
    left: 240px;
    top: 250px;
    width: 720px;
    height: 560px;
    background:
      radial-gradient(ellipse 22% 30% at 50% 28%, rgba(169,216,240,0.75), rgba(169,216,240,0) 100%),
      radial-gradient(ellipse 30% 40% at 72% 40%, rgba(191,230,176,0.8), rgba(191,230,176,0) 100%),
      radial-gradient(ellipse 26% 22% at 22% 58%, rgba(242,166,220,0.8), rgba(242,166,220,0) 100%),
      radial-gradient(ellipse 22% 20% at 80% 62%, rgba(242,166,220,0.7), rgba(242,166,220,0) 100%),
      radial-gradient(ellipse 22% 30% at 45% 82%, rgba(246,231,154,0.85), rgba(246,231,154,0) 100%);
  }
  .purity-badge {
    position: absolute;
    right: 190px;
    top: 62px;
    text-align: center;
    font-family: "Marcellus", serif;
    color: var(--ink);
  }
  .purity-badge__figure { font-size: 96px; line-height: 1; letter-spacing: -2px; }
  .purity-badge__words { font-size: 37px; line-height: 1.02; margin-top: 6px; }
  .product-title {
    position: absolute;
    left: 0;
    width: 1200px;
    top: 500px;
    text-align: center;
    font-family: "Open Sans", sans-serif;
  }
  .product-title__name { font-weight: 700; font-size: 92px; line-height: 1; letter-spacing: 1px; }
  .product-title__line { font-weight: 600; font-size: 44px; line-height: 1; margin-top: 18px; letter-spacing: 0.5px; }
  .product-copy {
    position: absolute;
    left: 0;
    width: 1200px;
    top: 828px;
    text-align: center;
    font-family: "Cormorant Garamond", serif;
    font-weight: 500;
    font-size: 30px;
    line-height: 36px;
    color: var(--ink-soft);
  }
  .net-weight {
    position: absolute;
    left: 0;
    width: 1200px;
    top: 1075px;
    text-align: center;
    font-family: "Marcellus", serif;
    font-size: 56px;
    color: var(--ink);
  }
</style>
</head>
<body>
  <main class="pouch-front">
    <div class="artwork-wash" role="img" aria-label="Watercolour wash in pink, blue, green and yellow with curling grey vine tendrils and leaves"></div>

    <div class="purity-badge">
      <div class="purity-badge__figure">100%</div>
      <div class="purity-badge__words">PURE &amp;<br>NATURAL</div>
    </div>

    <h1 class="product-title">
      <span class="product-title__name" style="display:block">SERENOVA</span>
      <span class="product-title__line" style="display:block">CALM INFUSION</span>
    </h1>

    <p class="product-copy">
      A unique blend of himalayan rock salt<br>
      and magnesium flakes<br>
      for the ultimate therapeutic bath soak.<br>
      Our Serenova Calm Infusion will detoxify<br>
      and revitalise your body.
    </p>

    <div class="net-weight">1kg</div>
  </main>
</body>
</html>
```